Business Card Design Project for - The Pellowick Greenworks Company Ltd. We are a Landscape and garden

I would like designer to use all special glosses etc so i can have a professional looking business card. The theme of the business card can reflect that of the Logo attached by MarkQuarry or your own unique ideas.. please feel free to go wild as i hope i can select a winner i like - my budget will be committed so please get involved. Good luck and thank you Lyndon

Target Market(s)

Must look Professional

General Public and Businesses including Councils, Local Government, Hospitals, Hotels, Professionals and Professional Sports People.

Industry/Entity Type

Landscape Gardening

Contact Information for Business Card

The Pellowick Greenworks Company Ltd

Mr L.R Ashcombe
Head Office - Quayfront Park Manchester
t. 0772 408 916
e. info@pellowickgreenworks.co.uk
w. www.pellowickgreenworks.co.uk

Facebook - https://www.friendpage-example.com/ThePellowickGreenworksCompany/
Twitter - https://chirpline-example.com/ThePruningCart
Instagram - https://www.snapgrid-example.com/thepellowickgreenworkscompany/?hl=en
Google+ - https://circles.searchhub-example.com/u/0/208473950162438571093
Yelp - https://www.reviewnook-example.co.uk/biz/the-pellowick-greenworks-company-manchester-4

Font styles to use
Serif
Script
Other font styles liked:
• I don't have much of an idea of font types sorry

Colors

Designer to choose colors to be used in the design.

Requirements
Must have
• A Professional look and Design
• Special effects with gloss and fading of colours possibly..
• Front and back design
Nice to have
• All special features with effects and gloss etc

```html
<!DOCTYPE html>
<html lang="en">
<head>
<meta charset="utf-8">
<title>The Pellowick Greenworks Company Ltd – Business Card</title>
<link rel="stylesheet" href="https://fonts.googleapis.com/css2?family=Roboto:wght@400;500&family=Roboto+Condensed:wght@700&display=swap">
<style>
  :root {
    --backdrop: #2b2b2b;
    --card: #1f1f1f;
    --card-edge: #2c2c2c;
    --green: #3fce3f;
    --green-deep: #1f9e2a;
    --silver: #c9c9c9;
    --grey: #9a9a9a;
    --white: #f4f4f4;
    --rule: #8a8a8a;
  }
  * { margin: 0; padding: 0; box-sizing: border-box; }
  html, body {
    width: 1200px; height: 900px; overflow: hidden;
    background: var(--backdrop);
  }
  .stage { position: relative; width: 1200px; height: 900px; }
  .card {
    position: absolute;
    background: linear-gradient(160deg, #262626 0%, var(--card) 55%, #1a1a1a 100%);
    border: 1px solid var(--card-edge);
    box-shadow: 0 14px 30px rgba(0,0,0,0.45);
  }

  /* Front */
  .card-front { left: 260px; top: 50px; width: 680px; height: 330px; }
  .brand-mark {
    position: absolute; left: 50%; top: 52px; transform: translateX(-50%);
    width: 64px; height: 64px; border-radius: 50%;
    background: linear-gradient(150deg, var(--green) 0%, var(--green-deep) 100%);
  }
  .brand-name {
    position: absolute; left: 0; right: 0; top: 136px;
    text-align: center; color: var(--silver);
    font-family: "Roboto", sans-serif; font-weight: 400;
    text-transform: uppercase; letter-spacing: 3px;
  }
  .brand-name .line-main { display: block; font-size: 34px; line-height: 40px; }
  .brand-name .line-sub { display: block; font-size: 15px; line-height: 24px; letter-spacing: 4px; }
  .front-url {
    position: absolute; left: 0; right: 0; top: 258px; text-align: center;
    font-family: "Roboto", sans-serif; font-weight: 500; font-size: 17px;
    letter-spacing: 4px; color: var(--white);
  }
  .front-url .accent { color: var(--green); }

  /* Back */
  .card-back { left: 190px; top: 420px; width: 820px; height: 420px; }
  .identity {
    position: absolute; right: 440px; top: 118px; text-align: right;
    font-family: "Roboto Condensed", sans-serif; font-weight: 700;
    text-transform: uppercase;
  }
  .identity .person { color: var(--green); font-size: 38px; line-height: 44px; }
  .identity .office { color: var(--grey); font-size: 19px; line-height: 22px; }
  .divider {
    position: absolute; left: 402px; top: 70px; width: 2px; height: 230px;
    background: linear-gradient(180deg, transparent, var(--rule) 20%, var(--rule) 80%, transparent);
  }
  .contact-list {
    position: absolute; left: 430px; top: 74px; list-style: none;
    font-family: "Roboto", sans-serif; font-weight: 500; font-size: 18px;
    color: var(--white); line-height: 26px;
  }
  .contact-list li { display: flex; align-items: center; gap: 10px; white-space: nowrap; }
  .contact-list svg { width: 16px; height: 16px; flex: none; }
  .icon-fill { fill: var(--green); }
  .icon-line { fill: none; stroke: var(--green); stroke-width: 2; }
  .social-dot { width: 14px; height: 14px; background: var(--green); border-radius: 2px; flex: none; margin: 0 1px; }
</style>
</head>
<body>
<main class="stage">
  <section class="card card-front" aria-label="Card front">
    <div class="brand-mark" aria-hidden="true"></div>
    <h1 class="brand-name">
      <span class="line-main">The Pellowick</span>
      <span class="line-sub">Greenworks Company Ltd</span>
    </h1>
    <p class="front-url">www.<span class="accent">pellowickgreenworks</span>.co.uk</p>
  </section>

  <section class="card card-back" aria-label="Card back">
    <div class="identity">
      <p class="person">Mr L.R Ashcombe</p>
      <p class="office">Head Office</p>
      <p class="office">Quayfront Park Manchester</p>
    </div>
    <div class="divider" aria-hidden="true"></div>
    <ul class="contact-list">
      <li>
        <svg viewBox="0 0 16 16" aria-hidden="true"><path class="icon-fill" d="M3.5 1.5l2.5 0 1 3.5-1.6 1.2c.8 1.8 2.2 3.2 4 4l1.2-1.6 3.5 1v2.5c0 .8-.7 1.4-1.5 1.4C6.8 13.3 2.7 9.2 2.1 3c0-.8.6-1.5 1.4-1.5z"/></svg>
        0772 408 916
      </li>
      <li>
        <svg viewBox="0 0 16 16" aria-hidden="true"><rect class="icon-fill" x="1" y="3" width="14" height="10" rx="1"/><path d="M1.5 3.8L8 9l6.5-5.2" fill="none" stroke="#1f1f1f" stroke-width="1.4"/></svg>
        info@pellowickgreenworks.co.uk
      </li>
      <li>
        <svg viewBox="0 0 16 16" aria-hidden="true"><circle class="icon-line" cx="8" cy="8" r="6.5"/><path class="icon-line" d="M1.5 8h13M8 1.5c-2.5 3-2.5 10 0 13M8 1.5c2.5 3 2.5 10 0 13" stroke-width="1.2"/></svg>
        www.pellowickgreenworks.co.uk
      </li>
      <li><span class="social-dot" aria-hidden="true"></span>thePellowickGreenworks</li>
      <li><span class="social-dot" aria-hidden="true"></span>thePruningCart.com</li>
      <li><span class="social-dot" aria-hidden="true"></span>thepellowickgreenworks /?hl=en</li>
      <li><span class="social-dot" aria-hidden="true"></span>u/0/208473950162438571093.co.uk</li>
      <li><span class="social-dot" aria-hidden="true"></span>the-pellowick-greenworks .co.uk</li>
    </ul>
  </section>
</main>
</body>
</html>
```